PowerPoint design of key models

We recently had a new PPT template created which we are very happy with. Now we want to have some of our key models on various pages in PPT to be reformatted and redesigned to match the other graphics of the new PT template. Can you please redesign the models and graphics so they have the same look and feel as the new template. I have included both files for you to work with. Thank you.

```html
<!DOCTYPE html>
<html lang="en">
<head>
<meta charset="utf-8">
<title>Key Models – Northline Consulting</title>
<link href="https://fonts.googleapis.com/css2?family=Poppins:wght@400;500;600;700;800&display=swap" rel="stylesheet">
<style>
:root{
  --navy:#141f4b;
  --mid:#1d6cc0;
  --light:#2aa9e2;
  --ink:#141f4b;
  --grey:#5d6170;
  --arrow:#d3d7de;
  --page:#dcdfe4;
  --white:#ffffff;
}
*{margin:0;padding:0;box-sizing:border-box}
html,body{width:1200px;height:5084px;overflow:hidden;background:var(--page);font-family:"Poppins",sans-serif;color:var(--ink)}
.deck{display:flex;flex-direction:column;gap:32.8px}
.slide{position:relative;width:1200px;height:820px;background:var(--white);overflow:hidden}
.brand{position:absolute;top:22px;right:34px;display:flex;align-items:center;gap:8px;font-weight:700;font-size:17px;color:var(--navy)}
.brand::before{content:"";width:18px;height:18px;border-radius:50%;background:var(--light)}
.title{position:absolute;left:80px;top:52px;font-size:44px;font-weight:700;line-height:1.15;color:var(--navy)}
.title::before{content:"";position:absolute;left:-50px;top:14px;width:32px;height:32px;border-radius:50%;background:var(--navy)}
.footer{position:absolute;left:0;right:0;bottom:28px;height:16px;background:linear-gradient(90deg,var(--light),var(--mid) 55%,var(--navy));display:flex;align-items:center;justify-content:center;font-size:9px;color:var(--white)}
.footer .num{position:absolute;right:34px;font-weight:600}
.abs{position:absolute}
svg{display:block}
/* slide 1 */
.label{font-weight:700;font-size:30px;line-height:1.1}
.questions{left:0;right:0;top:600px;text-align:center;font-size:22px;line-height:1.35;color:var(--navy)}
.questions strong{display:block;color:var(--light);font-size:26px;font-weight:700}
/* slide 2 */
.side-icon{width:52px;height:52px;border-radius:12px;left:56px;display:flex;align-items:center;justify-content:center}
/* slide 3 */
.trait{position:absolute;width:150px;height:150px;border-radius:50%;display:flex;align-items:center;justify-content:center;text-align:center;color:var(--white);font-weight:600;font-size:17px;line-height:1.2}
.bullets{position:absolute;font-size:15px;line-height:1.45;color:var(--grey);list-style:none}
.bullets li::before{content:"";display:inline-block;width:6px;height:6px;border-radius:50%;background:var(--light);margin-right:8px;vertical-align:middle}
/* slide 4 */
.subtitle{left:140px;top:290px;font-size:28px;font-weight:600;color:var(--navy)}
.chevrons{left:170px;top:400px;display:flex}
.chev{width:225px;height:120px;margin-right:-18px;display:flex;align-items:center;justify-content:center;color:var(--white);font-size:30px;font-weight:500;clip-path:polygon(0 0,85% 0,100% 50%,85% 100%,0 100%,15% 50%)}
.chev:first-child{clip-path:polygon(0 0,85% 0,100% 50%,85% 100%,0 100%)}
.chev b{font-weight:800;color:var(--light)}
/* slide 5 */
.hub{position:absolute;width:290px;height:290px;border-radius:50%;background:var(--navy);color:var(--white);display:flex;align-items:center;justify-content:center;text-align:center;font-size:26px;font-weight:700;line-height:1.25;padding:30px}
.row{position:absolute;left:600px;display:flex;gap:24px;align-items:flex-start}
.row-icon{width:76px;height:76px;border-radius:14px;background:var(--mid);display:flex;align-items:center;justify-content:center;flex:none}
.row h3{font-size:24px;font-weight:700;color:var(--navy)}
.row p{font-size:15px;color:var(--grey);line-height:1.45;max-width:420px}
/* slide 6 */
.node{position:absolute;width:170px;height:170px;border-radius:50%;display:flex;align-items:center;justify-content:center;text-align:center;color:var(--white);font-weight:600;font-size:19px;line-height:1.2;padding:18px}
.support{left:720px;top:350px;font-size:28px;line-height:1.3;color:var(--navy);font-weight:500;width:400px}
</style>
</head>
<body>
<main class="deck">

<!-- Value chain -->
<section class="slide">
  <div class="brand">Northline Consulting</div>
  <h1 class="title">Positioning on The Value Chain</h1>
  <svg class="abs" style="left:430px;top:150px" width="340" height="340" viewBox="0 0 340 340" aria-label="Value chain ring">
    <path d="M170 170 L0 170 A170 170 0 0 1 170 0 Z" fill="var(--navy)"/>
    <path d="M170 170 L170 0 A170 170 0 0 1 340 170 Z" fill="var(--light)"/>
    <path d="M170 170 L340 170 A170 170 0 0 1 170 340 Z" fill="var(--navy)"/>
    <path d="M170 170 L170 340 A170 170 0 0 1 0 170 Z" fill="var(--mid)"/>
    <path d="M170 0 V340 M0 170 H340" stroke="var(--white)" stroke-width="10"/>
    <circle cx="170" cy="170" r="88" fill="var(--white)"/>
    <g fill="none" stroke="var(--white)" stroke-width="3">
      <circle cx="90" cy="90" r="16"/><path d="M84 90 l5 5 9-10"/>
      <circle cx="250" cy="90" r="16"/><path d="M244 90 h12 M250 84 v12"/>
      <circle cx="250" cy="250" r="16"/><path d="M243 253 l7-7 7 7"/>
      <circle cx="90" cy="250" r="16"/><path d="M82 250 h16 M92 244 l6 6-6 6"/>
    </g>
    <circle cx="122" cy="170" r="9" fill="var(--light)"/>
    <text x="178" y="176" text-anchor="middle" font-family="Poppins, sans-serif" font-weight="700" font-size="15" fill="var(--navy)">Northline</text>
  </svg>
  <div class="abs label" style="left:315px;top:200px;text-align:right;color:var(--navy)">Order<br>Taker</div>
  <div class="abs label" style="left:790px;top:200px;color:var(--light)">Solutions<br>Provider</div>
  <div class="abs label" style="left:150px;top:420px;text-align:right;color:var(--mid);width:260px">Transactional<br>Trader</div>
  <div class="abs label" style="left:790px;top:420px;color:var(--navy)">Trusted<br>Advisor</div>
  <div class="abs questions"><strong>Questions</strong>Where are you today?<br>What does it take to move up?<br>What is your customer looking for?</div>
  <div class="footer">Copyright© Northline Consulting 2024<span class="num">32</span></div>
</section>

<!-- The stretch -->
<section class="slide">
  <div class="brand">Northline Consulting</div>
  <h1 class="title">The Stretch: Balancing Three<br>Competing Demands</h1>
  <div class="abs side-icon" style="top:232px;background:var(--navy)"><svg width="24" height="24" viewBox="0 0 24 24" fill="none" stroke="#fff" stroke-width="2"><rect x="4" y="3" width="16" height="18" rx="2"/><path d="M8 9h8M8 13h8M8 17h5"/></svg></div>
  <div class="abs side-icon" style="top:382px;background:var(--mid)"><svg width="24" height="24" viewBox="0 0 24 24" fill="none" stroke="#fff" stroke-width="2"><circle cx="8" cy="9" r="3"/><circle cx="16" cy="9" r="3"/><path d="M3 20c0-3 2-5 5-5s5 2 5 5M11 20c0-3 2-5 5-5s5 2 5 5"/></svg></div>
  <div class="abs side-icon" style="top:532px;background:var(--light)"><svg width="24" height="24" viewBox="0 0 24 24" fill="none" stroke="#fff" stroke-width="2"><circle cx="12" cy="8" r="4"/><path d="M4 21c0-4 4-7 8-7s8 3 8 7"/></svg></div>
  <svg class="abs" style="left:440px;top:150px" width="490" height="420" viewBox="0 0 490 420" aria-label="Task, team and individual triangle">
    <g stroke="var(--white)" stroke-width="8" stroke-linejoin="round">
      <path d="M245 4 L125 206 L365 206 Z" fill="var(--navy)"/>
      <path d="M125 206 L245 206 L245 412 L4 412 Z" fill="var(--mid)"/>
      <path d="M245 206 L365 206 L486 412 L245 412 Z" fill="var(--light)"/>
    </g>
    <g font-family="Poppins, sans-serif" font-weight="700" fill="var(--white)" text-anchor="middle">
      <text x="245" y="165" font-size="28">TASK</text>
      <text x="160" y="340" font-size="28">TEAM</text>
      <text x="340" y="340" font-size="26">INDIVIDUAL</text>
    </g>
    <g fill="none" stroke="var(--white)" stroke-width="2.5">
      <rect x="232" y="100" width="26" height="30" rx="3"/><path d="M238 110h14M238 118h14"/>
      <circle cx="152" cy="280" r="7"/><circle cx="170" cy="280" r="7"/>
      <circle cx="340" cy="278" r="8"/><path d="M326 300c0-8 6-12 14-12s14 4 14 12"/>
    </g>
  </svg>
  <div class="footer">Copyright© Northline Consulting 2024<span class="num">36</span></div>
</section>

<!-- Coaching traits -->
<section class="slide">
  <div class="brand">Northline Consulting</div>
  <h1 class="title">The 4 Essential Coaching Traits</h1>
  <svg class="abs" style="left:425px;top:165px" width="350" height="350" viewBox="0 0 350 350" aria-hidden="true">
    <circle cx="175" cy="175" r="150" fill="none" stroke="var(--arrow)" stroke-width="14"/>
  </svg>
  <div class="trait" style="left:525px;top:150px;background:var(--navy)">Questioning</div>
  <div class="trait" style="left:675px;top:265px;background:var(--light)">Measurement<br>&amp; Feedback</div>
  <div class="trait" style="left:525px;top:380px;background:var(--navy)">Behavioural<br>Flex</div>
  <div class="trait" style="left:375px;top:265px;background:var(--navy)">Presence</div>
  <ul class="bullets" style="left:700px;top:175px"><li>Ask, don't Tell</li><li>Use a Variety of<br>&nbsp;&nbsp;&nbsp;&nbsp;Questions</li></ul>
  <ul class="bullets" style="left:845px;top:305px"><li>5 levels of Listening</li><li>Be an Active<br>&nbsp;&nbsp;&nbsp;&nbsp;Listener</li></ul>
  <ul class="bullets" style="left:190px;top:275px"><li>Logged on</li><li>Mindful state</li><li>Manage climate</li><li>Observations</li></ul>
  <ul class="bullets" style="left:345px;top:460px"><li>From High control</li><li>To Low control</li></ul>
  <div class="footer">Copyright© Northline Consulting 2024<span class="num">37</span></div>
</section>

<!-- Call sequence -->
<section class="slide">
  <div class="brand">Northline Consulting</div>
  <h1 class="title">The Kestrel Call Sequence – P.R.E.S</h1>
  <div class="abs subtitle">This is how we structure our calls</div>
  <div class="abs chevrons">
    <div class="chev" style="background:var(--navy)"><span><b>P</b>lan</span></div>
    <div class="chev" style="background:var(--navy)"><span><b>R</b>ECRUIT</span></div>
    <div class="chev" style="background:var(--mid)"><span><b>E</b>xecute</span></div>
    <div class="chev" style="background:var(--navy)"><span><b>S</b>ustain</span></div>
  </div>
  <div class="footer">Copyright© Northline Consulting 2024<span class="num">38</span></div>
</section>

<!-- Integrated learning -->
<section class="slide">
  <div class="brand">Northline Consulting</div>
  <h1 class="title">An integrated approach to learning</h1>
  <svg class="abs" style="left:420px;top:230px" width="180" height="380" viewBox="0 0 180 380" aria-hidden="true">
    <path d="M0 190 H60 M60 30 V350 M60 30 H180 M60 190 H180 M60 350 H180" fill="none" stroke="var(--arrow)" stroke-width="4"/>
  </svg>
  <div class="hub" style="left:135px;top:275px">Developing High Performance Consultants</div>
  <div class="row" style="top:222px"><div class="row-icon"><svg width="34" height="34" viewBox="0 0 24 24" fill="none" stroke="#fff" stroke-width="2"><rect x="3" y="4" width="18" height="12" rx="1"/><path d="M8 20h8M12 16v4"/></svg></div><div><h3>Periodic Training</h3><p>Instalments of training over time:<br>Externally delivered workshops and internally delivered reinforcement</p></div></div>
  <div class="row" style="top:382px"><div class="row-icon"><svg width="34" height="34" viewBox="0 0 24 24" fill="none" stroke="#fff" stroke-width="2"><circle cx="7" cy="9" r="3"/><circle cx="17" cy="9" r="3"/><path d="M2 20c0-3 2-5 5-5s5 2 5 5M12 20c0-3 2-5 5-5s5 2 5 5"/></svg></div><div><h3>Objective Feedback<br><span style="font-size:18px">(via The Coaching Action Tool)</span></h3><p>Regular coaching sessions with your manager</p></div></div>
  <div class="row" style="top:542px"><div class="row-icon"><svg width="34" height="34" viewBox="0 0 24 24" fill="none" stroke="#fff" stroke-width="2"><circle cx="12" cy="8" r="4"/><path d="M4 21c0-4 4-7 8-7s8 3 8 7"/></svg></div><div><h3>Regular Coaching</h3><p>Objective feedback on strengths and development opportunities<br>using the Coaching Action Tool</p></div></div>
  <div class="footer">Copyright© Northline Consulting 2024<span class="num">39</span></div>
</section>

<!-- Development system -->
<section class="slide">
  <div class="brand">Northline Consulting</div>
  <h1 class="title">The Kestrel development system</h1>
  <svg class="abs" style="left:300px;top:210px" width="340" height="340" viewBox="0 0 340 340" aria-hidden="true">
    <circle cx="170" cy="170" r="150" fill="none" stroke="var(--arrow)" stroke-width="14"/>
  </svg>
  <div class="node" style="left:385px;top:150px;background:var(--mid)">10 Step Coaching Process</div>
  <div class="node" style="left:535px;top:295px;background:var(--light)">Coaching Action Tool</div>
  <div class="node" style="left:385px;top:440px;background:var(--navy)">RECRUIT BD Process</div>
  <div class="node" style="left:235px;top:295px;background:var(--navy)">PRES Call Sequence</div>
  <div class="abs support">Supporting your growth as a high performance consultant</div>
  <div class="footer">Copyright© Northline Consulting 2024<span class="num">40</span></div>
</section>

</main>
</body>
</html>
```